Website for The Tavery Parlour

I require a website for "The Tavery Parlour" which is a blog type business for 40+ year old women covering books, true crime, history, travel and food. It needs to support blog posts, links to social media including YouTube videos, Instagram, TikTok and Facebook. The background theme needs to be like that of a newspaper. Easy to navigate and to allow me to post blogs/videos.

```html
<!DOCTYPE html>
<html lang="en">
<head>
<meta charset="utf-8">
<title>The Tavery Parlour</title>
<link href="https://fonts.googleapis.com/css2?family=Playfair+Display:ital,wght@0,400;0,600;0,700;1,400;1,600&family=Poppins:wght@300;400;500&display=swap" rel="stylesheet">
<style>
:root{
  --paper:#ece8df;
  --paper-dark:#e2ddd2;
  --sage:#8b9986;
  --sage-dark:#76846f;
  --ink:#2b2a27;
  --muted:#6d6a63;
  --white:#ffffff;
  --line:#c9c4b8;
  --print-row:rgba(60,55,45,.045);
  --print-col:rgba(60,55,45,.07);
}
*{margin:0;padding:0;box-sizing:border-box}
html,body{width:1200px;height:3908px;overflow:hidden}
body{position:relative;background-color:var(--paper);
  background-image:
    repeating-linear-gradient(90deg,transparent 0 238px,var(--print-col) 238px 239px,transparent 239px 240px),
    repeating-linear-gradient(0deg,var(--print-row) 0 2px,transparent 2px 6px),
    repeating-linear-gradient(0deg,transparent 0 118px,rgba(60,55,45,.05) 118px 120px),
    radial-gradient(ellipse at 20% 30%,rgba(255,255,255,.35),transparent 55%),
    radial-gradient(ellipse at 80% 70%,rgba(120,110,90,.08),transparent 60%),
    linear-gradient(180deg,#efebe3,#e6e1d5 50%,#ece8df);
  font-family:"Poppins",sans-serif;color:var(--ink)}
.abs{position:absolute}
.serif{font-family:"Playfair Display",serif}
.photo{position:absolute}
.framed{border:6px solid var(--white);box-shadow:0 4px 14px rgba(0,0,0,.15)}
.btn{position:absolute;display:flex;align-items:center;justify-content:center;font-size:12px;border-radius:3px}
/* header */
.connect{left:148px;top:30px;font-family:"Playfair Display",serif;font-style:italic;font-size:14px}
.socials{display:flex;gap:10px}
.socials span{width:16px;height:16px;border-radius:50%;background:var(--sage-dark);display:block}
.menu{left:560px;top:10px;width:80px;font-size:13px;text-align:center;color:var(--muted)}
.menu::before,.menu::after{content:"";position:absolute;top:10px;width:14px;border-top:1px solid var(--muted)}
.menu::before{left:-8px}.menu::after{right:-8px}
.logo{left:0;width:1200px;top:92px;text-align:center;font-family:"Playfair Display",serif;font-size:30px;font-weight:600;color:var(--ink);letter-spacing:.5px}
.work{left:960px;top:8px;width:180px;height:28px;background:var(--sage);color:var(--white);font-size:12px}
.join{left:990px;top:92px;width:100px;font-family:"Playfair Display",serif;font-style:italic;font-size:14px;text-align:center;line-height:1.2}
/* hero */
.hero{left:0;top:168px;width:1200px;height:612px;background:linear-gradient(90deg,#8a8f83 0%,#a9ab9f 35%,#d8d3c6 55%,#b9b2a2 75%,#8d8677 100%)}
.hero-shade{left:0;top:168px;width:640px;height:612px;background:linear-gradient(90deg,rgba(60,64,56,.55),rgba(60,64,56,0))}
.because{left:120px;top:400px;transform:rotate(-90deg);transform-origin:left top;color:var(--white);font-size:13px;letter-spacing:3px;font-family:"Playfair Display",serif}
.hero-title{left:148px;top:350px;color:var(--white)}
.hero-title .big{font-size:66px;font-weight:700;line-height:1;letter-spacing:1px}
.hero-title .sub{font-size:36px;line-height:1.2;margin-top:4px}
.hero-copy{left:148px;top:470px;width:430px;color:var(--white);font-size:11px;line-height:1.7;font-weight:300}
.hero-btn{left:148px;top:578px;width:120px;height:32px;background:var(--white);color:var(--ink)}
/* wisdom */
.vertical{left:64px;top:1350px;transform:rotate(-90deg);transform-origin:left top;font-family:"Playfair Display",serif;font-style:italic;font-weight:600;font-size:20px;line-height:1.1;color:var(--ink)}
.wisdom-h{left:688px;top:948px;font-size:30px;font-style:italic;font-weight:600;line-height:1.2}
.wisdom-p{left:688px;top:1050px;width:400px;font-size:11.5px;line-height:1.9;color:var(--muted)}
.wisdom-btn{left:688px;top:1288px;width:120px;height:32px;background:var(--sage);color:var(--white)}
/* topics */
.section-h{left:0;width:1200px;text-align:center;font-size:30px;font-style:italic;font-weight:600}
.tabs{left:280px;top:1584px;width:640px;height:28px;display:flex;justify-content:space-between;align-items:center}
.tabs::before{content:"";position:absolute;left:0;right:0;top:14px;border-top:1px solid var(--line)}
.tab{position:relative;background:var(--paper);padding:4px 22px;font-size:12px;color:var(--muted)}
.tab.active{border:1px solid var(--ink);color:var(--ink);background:var(--white)}
.card{position:absolute;width:220px;height:316px;background:var(--white);padding:8px;box-shadow:0 2px 8px rgba(0,0,0,.08)}
.card .img{height:118px;width:100%}
.tag{display:inline-block;margin-top:10px;background:var(--sage);color:var(--white);font-size:9px;padding:2px 8px;border-radius:2px}
.card p{font-size:10.5px;line-height:1.6;color:var(--muted);margin-top:8px}
.card .name{font-size:13px;font-weight:500;color:var(--ink);margin-top:6px}
.meta{position:absolute;left:8px;right:8px;bottom:12px;display:flex;align-items:center;gap:6px;font-size:9px;color:var(--muted);border-top:1px solid #eee;padding-top:8px}
.meta i{width:18px;height:18px;border-radius:50%;background:#b7a995;display:block}
.meta b{font-weight:400;margin-left:auto}
.dots{left:0;width:1200px;top:2340px;display:flex;justify-content:center;gap:10px}
.dots span{width:7px;height:7px;border-radius:50%;background:#c0bbb0}
.dots .on{background:var(--ink)}
/* stories */
.stories-h{left:148px;top:2462px;width:580px;font-size:28px;font-style:italic;font-weight:600;white-space:nowrap}
.stories-p{left:148px;top:2512px;width:540px;font-size:11.5px;line-height:1.9;color:var(--muted)}
/* form */
.field{position:absolute;background:var(--white);border:1px solid #ddd8cd;height:36px;font-size:11px;color:var(--muted);padding:10px 14px}
.submit{left:220px;top:3460px;width:760px;height:34px;background:var(--sage);color:var(--white);font-size:13px}
/* footer */
.footer{left:0;top:3600px;width:1200px;height:308px;background:var(--sage);color:var(--white)}
.f-logo{left:148px;top:42px;font-size:26px;font-weight:600}
.f-text{left:148px;top:92px;width:240px;font-size:10.5px;line-height:1.7;opacity:.9}
.f-social{left:148px;top:160px}
.f-social span{background:var(--white)}
.f-col h4{font-family:"Playfair Display",serif;font-size:17px;font-weight:600;margin-bottom:16px}
.f-col li{list-style:none;font-size:10.5px;margin-bottom:10px;opacity:.9}
.f-news h4{font-family:"Playfair Display",serif;font-style:italic;font-size:22px;font-weight:400;margin-bottom:6px}
.f-news p{font-size:10.5px;line-height:1.6;width:290px;opacity:.9}
.f-input{left:770px;top:130px;width:170px;height:32px;border:1px solid rgba(255,255,255,.8);font-size:10.5px;padding:8px 12px;background:var(--white);color:var(--muted)}
.f-sub{left:950px;top:130px;width:100px;height:32px;border:1px solid var(--white);color:var(--white)}
.f-bar{left:0;top:262px;width:1200px;border-top:1px solid rgba(255,255,255,.4);padding-top:12px;text-align:center;font-size:10px}
</style>
</head>
<body>

<header>
  <div class="abs connect">Let's Connect</div>
  <div class="abs socials" style="left:148px;top:56px"><span></span><span></span><span></span></div>
  <div class="abs menu">Menu</div>
  <div class="abs logo">The Tavery Parlour</div>
  <div class="btn work">let's work together</div>
  <div class="abs join">Join The Newsletter</div>
</header>

<section class="hero-block">
  <div class="photo hero" role="img" aria-label="Smiling woman in glasses standing by a sunlit window"></div>
  <div class="abs hero-shade"></div>
  <div class="abs because">BECAUSE</div>
  <div class="abs hero-title serif">
    <div class="big">LIFE GETS</div>
    <div class="sub">More Interesting After 40</div>
  </div>
  <p class="abs hero-copy">Stories, ideas and honest conversation for women who are only getting started. Books, travel, history, food and true crime, gathered for curious minds who love to read and share.</p>
  <div class="btn hero-btn">Learn More</div>
</section>

<section class="wisdom">
  <div class="photo" style="left:0;top:888px;width:368px;height:184px;background:linear-gradient(135deg,#a28f78,#d9cfc0 60%,#8e8070)" role="img" aria-label="Woman working on a laptop at a bright desk"></div>
  <div class="photo framed" style="left:380px;top:992px;width:280px;height:280px;background:linear-gradient(160deg,#e4e1da,#c8cfc4 50%,#9fae9a)" role="img" aria-label="Two women talking in a light office"></div>
  <div class="photo framed" style="left:220px;top:1048px;width:160px;height:332px;background:linear-gradient(180deg,#d7d1c6,#b9a58c 60%,#6e6558)" role="img" aria-label="Woman seated in a chair with a laptop"></div>
  <div class="abs vertical">Rooted in truth, told<br>with heart</div>
  <h2 class="abs wisdom-h serif">Because wisdom deserves<br>a voice</h2>
  <p class="abs wisdom-p">Every season of life brings its own lessons, and this is a place to share them. Here you will find thoughtful writing on the books we treasure, the places we wander and the history that shapes us. Each post is written to inform, to entertain and to spark a good conversation over coffee. Pull up a chair, settle in and read at your own pace. New stories arrive every week, along with short videos and reading lists picked with care.</p>
  <div class="btn wisdom-btn">Learn More</div>
</section>

<section class="topics">
  <h2 class="abs section-h serif" style="top:1504px">A World of Topics, A Lifetime of Stories</h2>
  <nav class="abs tabs">
    <span class="tab active">Travel</span><span class="tab">Books</span><span class="tab">History</span><span class="tab">True Crime</span><span class="tab">Food</span>
  </nav>

  <article class="card" style="left:148px;top:1660px"><div class="img" style="background:linear-gradient(160deg,#c7b59b,#8d6f52)" role="img" aria-label="Traveller with luggage at a station"></div><span class="tag">Travel</span><p>This story is designed to make good reading and add real value for you, the reader.</p><div class="name">Marian Holloway</div><div class="meta"><i></i>Travel Desk<b>Jan 12, 2025</b></div></article>
  <article class="card" style="left:378px;top:1660px"><div class="img" style="background:linear-gradient(160deg,#9fb6c9,#d6c2a2)" role="img" aria-label="Woman seated on a hillside at sunset"></div><span class="tag">Travel</span><p>This story is designed to make good reading and add real value for you, the reader.</p><div class="name">Greta Pembly</div><div class="meta"><i></i>Travel Desk<b>Jan 12, 2025</b></div></article>
  <article class="card" style="left:608px;top:1660px"><div class="img" style="background:linear-gradient(160deg,#e5c48a,#8f7a5e)" role="img" aria-label="Woman at a waterside railing"></div><span class="tag">Travel</span><p>This story is designed to make good reading and add real value for you, the reader.</p><div class="name">Delia Fairbrook</div><div class="meta"><i></i>Travel Desk<b>Jan 12, 2025</b></div></article>
  <article class="card" style="left:838px;top:1660px"><div class="img" style="background:linear-gradient(180deg,#a7c2d8,#6f8f6a)" role="img" aria-label="Mountain lake landscape"></div><span class="tag">Travel</span><p>This story is designed to make good reading and add real value for you, the reader.</p><div class="name">Rosa Whitcombe</div><div class="meta"><i></i>Travel Desk<b>Jan 12, 2025</b></div></article>

  <article class="card" style="left:148px;top:1996px"><div class="img" style="background:linear-gradient(160deg,#7f96b8,#caa57a)" role="img" aria-label="Woman with a camera in a city street"></div><span class="tag">Travel</span><p>This story is designed to make good reading and add real value for you, the reader.</p><div class="name">Marian Holloway</div><div class="meta"><i></i>Travel Desk<b>Jan 12, 2025</b></div></article>
  <article class="card" style="left:378px;top:1996px"><div class="img" style="background:linear-gradient(160deg,#e8b27a,#7a8fb0)" role="img" aria-label="Woman in a colourful coat outdoors"></div><span class="tag">Travel</span><p>This story is designed to make good reading and add real value for you, the reader.</p><div class="name">Greta Pembly</div><div class="meta"><i></i>Travel Desk<b>Jan 12, 2025</b></div></article>
  <article class="card" style="left:608px;top:1996px"><div class="img" style="background:linear-gradient(160deg,#b5a184,#5f584c)" role="img" aria-label="Traveller resting by a stone wall"></div><span class="tag">Travel</span><p>This story is designed to make good reading and add real value for you, the reader.</p><div class="name">Delia Fairbrook</div><div class="meta"><i></i>Travel Desk<b>Jan 12, 2025</b></div></article>
  <article class="card" style="left:838px;top:1996px"><div class="img" style="background:linear-gradient(160deg,#d9d6cf,#8e8a80)" role="img" aria-label="Woman reading by a large window"></div><span class="tag">Travel</span><p>This story is designed to make good reading and add real value for you, the reader.</p><div class="name">Rosa Whitcombe</div><div class="meta"><i></i>Travel Desk<b>Jan 12, 2025</b></div></article>

  <div class="abs dots"><span></span><span></span><span class="on"></span><span></span><span></span></div>
</section>

<section class="stories">
  <h2 class="abs stories-h serif">A World of Topics, A Lifetime of Stories</h2>
  <p class="abs stories-p">From a quiet morning with a favourite novel to a long lunch in a new city, these pages celebrate the pleasures that grow richer with time. Explore recipes, reading notes and travel diaries, all shared by women who know that the best chapters are still being written.</p>
  <div class="photo" style="left:760px;top:2460px;width:288px;height:250px;background:linear-gradient(150deg,#7a5a3e,#c9a478 55%,#3f3328)" role="img" aria-label="Hands holding a book beside a cup of tea"></div>
  <div class="photo" style="left:0;top:2660px;width:220px;height:160px;background:linear-gradient(150deg,#e7d6bf,#c79a5e 60%,#8d5b36)" role="img" aria-label="Woman enjoying breakfast with fruit and coffee"></div>
  <div class="photo framed" style="left:220px;top:2660px;width:380px;height:340px;background:linear-gradient(160deg,#6f6a60,#d8c7a8 55%,#8e7558)" role="img" aria-label="Open book held in hands on a wooden table"></div>
  <div class="photo framed" style="left:608px;top:2632px;width:140px;height:248px;background:linear-gradient(180deg,#ede7dc,#cbb394 60%,#8f7a60)" role="img" aria-label="Woman reading with a cup in a cosy room"></div>
  <div class="photo" style="left:752px;top:2800px;width:124px;height:200px;background:linear-gradient(160deg,#e0c28a,#b06a3c 60%,#5e3a22)" role="img" aria-label="Plated dish of homemade food"></div>
</section>

<section class="contact">
  <h2 class="abs section-h serif" style="top:3120px">A World of Topics, A Lifetime of Stories</h2>
  <div class="field" style="left:220px;top:3208px;width:370px">First Name</div>
  <div class="field" style="left:610px;top:3208px;width:370px">Last Name</div>
  <div class="field" style="left:220px;top:3260px;width:370px">Phone Number</div>
  <div class="field" style="left:610px;top:3260px;width:370px">Email</div>
  <div class="field" style="left:220px;top:3312px;width:760px;height:130px">Messages</div>
  <div class="btn submit">Submit</div>
</section>

<footer class="abs footer">
  <div class="abs f-logo serif">The Tavery Parlour</div>
  <p class="abs f-text">Fresh stories, honest reviews and good company for women over forty. New posts and videos every week.</p>
  <div class="abs socials f-social"><span></span><span></span><span></span><span></span></div>
  <div class="abs f-col" style="left:460px;top:44px"><h4>About Us</h4><ul><li>Meet the Writer</li><li>Latest Stories</li><li>Videos</li><li>Contact</li></ul></div>
  <div class="abs f-col" style="left:590px;top:44px"><h4>Topics</h4><ul><li>Books</li><li>True Crime</li><li>History</li><li>Travel</li></ul></div>
  <div class="abs f-news" style="left:770px;top:40px"><h4>Newsletter</h4><p>Get new posts and reading picks in your inbox each week.</p></div>
  <div class="abs f-input">Email</div>
  <div class="btn f-sub">Subscribe</div>
  <div class="abs f-bar">Copyright © The Tavery Parlour</div>
</footer>

</body>
</html>
```